Email Banner for Technology Company

We need a new email banner. The purpose of the email banner is to make us look more professional as a business and keep all communications with clients uniform. The previous designs which we have included below have now become outdated as our brand has developed and we need the new banner to become more aligned and modern.

We are a marketing organization that specialises in lead generation, email newsletters are sent to prospects on a regular basis. Therefore, it is important that we have an aesthetically pleasing banner as this is the first real impression prospects have our business. First impressions matter.

We are looking for a new email banner design as the current design is now outdated and does not reflect who we are as a business.

The new banners are required for launch at the start of Q2.

There is future work in the pipeline for the winning design. We have multiple industry sites that will require the new design as well as creating each of these in multiple languages.

The design must include the Zevomarkly wording the tagline 'The Ultimate Research Library for Technology Pro's.
It needs to be creative and fun but still remain professional, sticking with the colour theme that already exists.

Requirements
Must have
• The design must include the Zevomarkly wording the tagline 'The Ultimate Research Library for Technology Pro's.

```html
<!DOCTYPE html>
<html lang="en">
<head>
<meta charset="UTF-8">
<title>Zevomarkly Email Banner</title>
<link href="https://fonts.googleapis.com/css2?family=Montserrat:wght@600;700&display=swap" rel="stylesheet">
<style>
  :root {
    --page-bg: #ecedee;
    --navy: #1e3648;
    --cyan: #1ab0d3;
    --white: #ffffff;
    --art-light: #3c8e9a;
    --art-dark: #27535f;
  }
  * { margin: 0; padding: 0; box-sizing: border-box; }
  html, body {
    width: 1200px;
    height: 432px;
    overflow: hidden;
    background: var(--page-bg);
  }
  .banner {
    position: absolute;
    left: 30px;
    top: 122px;
    width: 1140px;
    height: 188px;
    background: var(--navy);
    overflow: hidden;
  }
  .banner__shapes {
    position: absolute;
    inset: 0;
  }
  .banner__art {
    position: absolute;
    left: 40px;
    top: 26px;
    width: 236px;
    height: 142px;
    border-radius: 6px;
    background: linear-gradient(135deg, var(--art-light) 0%, var(--art-dark) 100%);
  }
  .banner__tagline {
    position: absolute;
    left: 312px;
    top: 45px;
    font-family: "Montserrat", sans-serif;
    font-weight: 700;
    font-size: 36px;
    line-height: 48px;
    letter-spacing: -0.2px;
    color: var(--white);
  }
  .banner__tagline .accent { color: var(--cyan); }
  .brand {
    position: absolute;
    left: 988px;
    top: 44px;
    width: 100px;
    height: 100px;
    border-radius: 50%;
    background: var(--white);
    display: flex;
    align-items: center;
    justify-content: center;
  }
  .brand__name {
    font-family: "Montserrat", sans-serif;
    font-weight: 700;
    font-size: 14px;
    color: var(--navy);
  }
</style>
</head>
<body>
  <div class="banner">
    <svg class="banner__shapes" width="1140" height="188" viewBox="0 0 1140 188" aria-hidden="true">
      <polygon points="942,0 1140,0 1140,188 868,188" fill="var(--white)"/>
      <polygon points="952,0 1140,0 1140,188 878,188" fill="var(--cyan)"/>
    </svg>
    <div class="banner__art" role="img" aria-label="Isometric illustration of a laptop with documents and a server tower"></div>
    <h1 class="banner__tagline">
      The Ultimate <span class="accent">Research</span><br>
      <span class="accent">Library</span> for Technology Pro's
    </h1>
    <div class="brand">
      <span class="brand__name">Zevomarkly</span>
    </div>
  </div>
</body>
</html>
```